Web Design for photo printing service

Hi
I am looking for a new web design theme for our almost ready website http://glerhorn.tqzs.net, it will soon be launched under the name: www.zuba-web.is. (ZUBA means: Zest Under Bright Arches)

This is a website focused on printing photo products like: photo books, Greeting cards, posters, etc.

The whole theme should be playful, fun, creative. The marketing will be is that Life is fun, keep your memories. remember the good time etc.

So what I am looking for is a simple, yet colorful theme, easy to use.

We will be running max 4- 6 product groups, all extra info should be on the button,
expect shopping chart and sign in should be on top.

Extra feature:
Once a year during christmas, the web will turn on christmas outfit, it transforms
to Christmas looking Web. So a X-mas version would be fun to see !

Young people 20-35, young families.

Printing

• Fun looking colorful design, simple to use.
• Dark heavy look

```html
<!DOCTYPE html>
<html lang="en">
<head>
<meta charset="utf-8">
<title>ZUBA – Photo Printing</title>
<link rel="stylesheet" href="https://fonts.googleapis.com/css2?family=Lato:wght@400;700;900&display=swap">
<style>
:root{
  --green:#1a9b78;
  --pink:#e8177a;
  --blue:#18a0c6;
  --orange:#f39233;
  --purple:#a3218e;
  --lime:#a3c83b;
  --dark:#404041;
  --band:#e6e7e8;
  --ink:#222;
  --line:#c9c9c9;
  --white:#fff;
}
*{margin:0;padding:0;box-sizing:border-box}
html,body{width:1200px;height:747px;overflow:hidden;background:var(--white)}
body{position:relative;font-family:'Lato',sans-serif;color:var(--ink)}
.brand{position:absolute;left:0;width:1200px;top:14px;text-align:center;font-weight:900;font-size:44px;letter-spacing:2px;color:var(--purple);line-height:50px}
.brand-dot{display:inline-block;width:12px;height:12px;border-radius:50%;background:var(--pink);margin-left:6px;vertical-align:middle}
.cart-mini{position:absolute;left:818px;top:34px;width:132px;height:28px;border:1px solid var(--line);border-radius:2px;background:#f7f7f7;text-align:center;font-size:10px;line-height:12px;padding-top:2px;color:#333}
.cart-mini strong{display:block;font-size:11px;font-weight:700}
.rule-top{position:absolute;left:514px;top:83px;width:165px;height:1px;background:var(--line)}
.nav{position:absolute;left:0;width:1200px;top:93px;display:flex;justify-content:center;align-items:center;font-size:10.5px;text-transform:uppercase}
.nav a{color:var(--ink);text-decoration:none;padding:2px 6px}
.nav a.active{background:var(--green);color:var(--white)}
.nav .sep{margin:0 10px;font-size:9px}
.rule-nav{position:absolute;left:250px;top:118px;width:700px;height:1px;background:var(--line)}
.band{position:absolute;left:0;top:142px;width:1200px;height:518px;background:var(--band)}
.hero{position:absolute;left:250px;top:157px;width:700px;height:144px;border:2px solid var(--white);background:linear-gradient(90deg,#6b4a2e 0%,#c98a4e 35%,#e0a86a 60%,#a46a3a 100%);box-shadow:0 1px 2px rgba(0,0,0,.15)}
.hero-title{position:absolute;right:28px;bottom:16px;font-size:34px;font-weight:700;color:rgba(255,255,255,.92)}
.card{position:absolute;width:224px;height:158px;background:var(--white)}
.tile{position:absolute;left:6px;top:8px;width:76px;height:114px;color:var(--white);text-align:center}
.tile svg{position:absolute;left:8px;top:8px}
.price{position:absolute;left:0;width:76px;top:74px;font-size:12.5px;font-weight:700;line-height:13px}
.card h2{position:absolute;left:88px;top:12px;font-size:13px;font-weight:700;text-transform:uppercase;line-height:13.5px}
.card p{position:absolute;left:90px;top:36px;width:128px;font-family:Arial,sans-serif;font-size:8.6px;line-height:13.6px;color:#333}
.card h2.two-line + p{top:49px}
.more{position:absolute;left:0;bottom:0;width:224px;height:28px;background:var(--dark);color:var(--white);font-size:13px;font-weight:700;text-align:center;line-height:28px}
.cart-art{position:absolute;left:6px;top:7px;width:211px;height:114px;background:radial-gradient(ellipse at 50% 75%,#f2dc55 0%,#e8c93a 35%,var(--purple) 36%)}
.cart-art .label{position:absolute;left:0;width:211px;top:66px;text-align:center;color:#5a4a1a;font-size:18px;font-weight:700;line-height:20px}
.cart-art .label span{display:block;font-size:12px;font-weight:400}
.acct{position:absolute;top:126px;width:104px;height:28px;background:var(--dark);color:var(--white);font-size:11px;font-weight:700;text-align:center;line-height:28px}
.footer-links{position:absolute;left:0;width:1200px;top:679px;text-align:center;font-family:Arial,sans-serif;font-size:9px;text-transform:uppercase}
.footer-links span{margin:0 9px}
.copy{position:absolute;left:0;width:1200px;top:701px;text-align:center;font-family:Arial,sans-serif;font-size:9px}
</style>
</head>
<body>
<div class="brand">ZUBA<span class="brand-dot"></span></div>
<div class="cart-mini"><strong>My Cart</strong>0 Articles • kr 0.00</div>
<div class="rule-top"></div>
<nav class="nav">
  <a class="active">Photo Book</a><span class="sep">●</span>
  <a>Calendars</a><span class="sep">●</span>
  <a>Osters</a><span class="sep">●</span>
  <a>Map</a><span class="sep">●</span>
  <a>Printed Photographs</a><span class="sep">●</span>
  <a>Our Price</a>
</nav>
<div class="rule-nav"></div>

<div class="band"></div>
<div class="hero" role="img" aria-label="Silhouettes of women with parasols walking on a beach at sunset, with framed photo prints on the left">
  <div class="hero-title">Zest Under Bright Arches</div>
</div>

<div class="card" style="left:250px;top:315px">
  <div class="tile" style="background:var(--pink)">
    <svg width="60" height="48" viewBox="0 0 60 48" fill="none" stroke="#fff" stroke-width="3"><rect x="4" y="4" width="48" height="38"/><rect x="10" y="10" width="48" height="36" fill="var(--pink)"/><circle cx="24" cy="21" r="4" fill="#fff" stroke="none"/><path d="M14 42 L28 28 L36 36 L44 26 L54 42 Z" fill="#fff" stroke="none"/></svg>
    <div class="price">From kr<br>2000,00</div>
  </div>
  <h2>Photo Books</h2>
  <p>Lorem Ipsum has been the industry's standard dummy text ever since the 1500s, when an unknown printer took a galley of type and scrambled it to make a type specimen book.</p>
  <div class="more">Want to Know More</div>
</div>

<div class="card" style="left:489px;top:315px">
  <div class="tile" style="background:var(--blue)">
    <svg width="56" height="48" viewBox="0 0 56 48" fill="none" stroke="#fff" stroke-width="3"><rect x="4" y="4" width="48" height="40" rx="2"/><line x1="4" y1="13" x2="52" y2="13"/><g fill="#fff" stroke="none"><rect x="12" y="19" width="5" height="4"/><rect x="20" y="19" width="5" height="4"/><rect x="28" y="19" width="5" height="4"/><rect x="36" y="19" width="5" height="4"/><rect x="12" y="26" width="5" height="4"/><rect x="20" y="26" width="5" height="4"/><rect x="28" y="26" width="5" height="4"/><rect x="36" y="26" width="5" height="4"/><rect x="12" y="33" width="5" height="4"/><rect x="20" y="33" width="5" height="4"/><rect x="28" y="33" width="5" height="4"/></g></svg>
    <div class="price">From kr<br>1500,00</div>
  </div>
  <h2>Calendars</h2>
  <p>Lorem Ipsum has been the industry's standard dummy text ever since the 1500s, when an unknown printer took a galley of type and scrambled it to make a type specimen book.</p>
  <div class="more">Want to Know More</div>
</div>

<div class="card" style="left:726px;top:315px">
  <div class="tile" style="background:var(--orange)">
    <svg width="60" height="48" viewBox="0 0 60 48"><path d="M4 10 H18 L22 4 H40 L44 10 H56 V44 H4 Z" fill="#fff"/><circle cx="31" cy="27" r="11" fill="var(--orange)"/><circle cx="31" cy="27" r="6" fill="#fff"/><circle cx="31" cy="27" r="3" fill="var(--orange)"/></svg>
    <div class="price">From kr<br>495,00</div>
  </div>
  <h2>Posters</h2>
  <p>Lorem Ipsum has been the industry's standard dummy text ever since the 1500s, when an unknown printer took a galley of type and scrambled it to make a type specimen book.</p>
  <div class="more">Want to Know More</div>
</div>

<div class="card" style="left:250px;top:488px">
  <div class="tile" style="background:var(--purple)">
    <svg width="56" height="52" viewBox="0 0 56 52"><path d="M4 6 L18 12 L32 6 L48 12 V48 L32 42 L18 48 L4 42 Z" fill="#fff"/><path d="M32 4 C24 4 20 10 22 16 C24 22 32 32 32 32 C32 32 40 22 42 16 C44 10 40 4 32 4 Z" fill="#fff" stroke="var(--purple)" stroke-width="2"/><circle cx="32" cy="14" r="3.5" fill="var(--purple)"/></svg>
    <div class="price">From kr<br>2000,00</div>
  </div>
  <h2>Map</h2>
  <p>Lorem Ipsum has been the industry's standard dummy text ever since the 1500s, when an unknown printer took a galley of type and scrambled it to make a type specimen book.</p>
  <div class="more">Want to Know More</div>
</div>

<div class="card" style="left:489px;top:488px">
  <div class="tile" style="background:var(--lime)">
    <svg width="60" height="48" viewBox="0 0 60 48"><path d="M4 6 H56 V32 C50 36 46 30 40 34 V44 H20 V34 C14 30 10 36 4 32 Z" fill="#fff"/><rect x="18" y="14" width="24" height="20" fill="var(--lime)"/><path d="M20 32 L28 22 L33 28 L37 24 L40 32 Z" fill="#fff"/></svg>
    <div class="price">From kr<br>2000,00</div>
  </div>
  <h2 class="two-line">Printed<br>Photographs</h2>
  <p>dummy text ever since the 1500s, when an unknown printer took a galley of type and scrambled it to make a type specimen book.</p>
  <div class="more">Want to Know More</div>
</div>

<div class="card" style="left:726px;top:488px">
  <div class="cart-art" role="img" aria-label="Yellow shopping folder filled with photo prints on a purple background">
    <div class="label">My Cart<span>0 Articles • kr 0.00</span></div>
  </div>
  <div class="acct" style="left:6px">Create an Account</div>
  <div class="acct" style="left:113px">Sign In</div>
</div>

<div class="footer-links">
  <span>Home</span>I<span>The Small Print</span>I<span>What do you want to know</span>I<span>Rates</span>I<span>About Us</span>I<span>Contact</span>
</div>
<div class="copy">© 2013 ZUBA.</div>
</body>
</html>
```